Quorvel Landing page redesign

We are looking for a landing page redesign before we officially launch. We want to incorporate the information already on the site at www.Quorvel-example.com landing page but make it more inviting. There needs to be a sign up section along with clearly stating what we do. Having a place for sample profiles and linking to our blog and podcast is option. More information about all we will be doing is at Quorvel is on the landing page and also on the blog.

Target Market(s)

35 years old and up.

Coding

Coded - Design and coding required

Number of Pages Required

1 page

Requirements
Must have
• The top bar and the bottom bar (with the privacy policy, etc)
• Sign in/up section.
• I don't want to give to much here because I want designers to be creative.
Nice to have
• Prefer not to have a landing page that requires a lot of scrolling at all.

```html
<!DOCTYPE html>
<html lang="en">
<head>
<meta charset="UTF-8">
<title>Quorvel</title>
<link href="https://fonts.googleapis.com/css2?family=Nunito+Sans:wght@400;600;700&display=swap" rel="stylesheet">
<style>
  :root {
    --page-gray: #595959;
    --white: #ffffff;
    --accent-orange: #ef9150;
    --panel-yellow: rgba(241, 199, 42, 0.86);
    --button-teal: #27e9d3;
    --text-dark: #4a4a4a;
    --divider: #f0a470;
  }
  * { margin: 0; padding: 0; box-sizing: border-box; }
  html, body {
    width: 1200px; height: 737px; overflow: hidden;
    background: var(--page-gray);
    font-family: "Nunito Sans", Arial, sans-serif;
  }
  .canvas { position: relative; width: 1200px; height: 737px; }

  .hero {
    position: absolute; left: 86px; top: 0; width: 1028px; height: 493px;
    background:
      radial-gradient(ellipse at 60% 20%, #e9a869 0%, transparent 45%),
      radial-gradient(ellipse at 20% 70%, #b5583a 0%, transparent 50%),
      linear-gradient(160deg, #8c5a38 0%, #c57f4c 40%, #a8603f 70%, #6d3f2a 100%);
  }

  .brand { position: absolute; color: var(--white); font-weight: 600; }
  .brand--header { left: 117px; top: 41px; font-size: 21px; line-height: 28px; }
  .brand--footer { left: 117px; top: 684px; font-size: 15px; line-height: 20px; }

  .main-nav a {
    position: absolute; top: 47px; color: var(--white); text-decoration: none;
    font-size: 13px; font-weight: 700; letter-spacing: 0.05em;
  }

  .signup-panel {
    position: absolute; left: 360px; top: 138px; width: 480px; height: 288px;
    background: var(--panel-yellow); color: var(--white); text-align: center;
  }
  .signup-panel h1 { font-size: 24px; font-weight: 600; letter-spacing: 0.03em; margin-top: 33px; }
  .signup-panel .lead { font-size: 14px; font-weight: 600; line-height: 21px; margin-top: 7px; }
  .signup-panel h2 { font-size: 17px; font-weight: 600; letter-spacing: 0.03em; margin-top: 37px; }
  .email-field {
    position: absolute; left: 81px; top: 194px; width: 219px; height: 50px;
    background: var(--white); border: none; padding-left: 13px;
    font-family: inherit; font-size: 13px; color: var(--text-dark); letter-spacing: 0.03em;
  }
  .email-field::placeholder { color: #333; }
  .subscribe-button {
    position: absolute; left: 317px; top: 194px; width: 119px; height: 45px;
    background: var(--button-teal); border: 1px solid rgba(255,255,255,0.8);
    font-family: inherit; font-size: 12.5px; letter-spacing: 0.08em; color: #3a3a3a;
  }

  .features {
    position: absolute; left: 86px; top: 493px; width: 1028px; height: 173px;
    background: var(--white);
  }
  .feature {
    position: absolute; top: 38px; height: 86px; text-align: center; transform: translateX(-50%);
    width: 200px;
  }
  .feature h3 { font-size: 24px; font-weight: 400; color: var(--accent-orange); line-height: 30px; }
  .feature p { font-size: 14.5px; color: var(--text-dark); line-height: 21px; margin-top: 5px; }
  .divider { position: absolute; top: 38px; width: 1px; height: 86px; background: var(--divider); }

  .footer-links {
    position: absolute; right: 122px; top: 685px; display: flex; gap: 13px;
  }
  .footer-links a { color: var(--white); text-decoration: none; font-size: 10.5px; font-weight: 600; }
</style>
</head>
<body>
<div class="canvas">
  <div class="hero" role="img" aria-label="Photo of a parent and children lying under a blanket fort looking at a tablet"></div>

  <header class="site-header">
    <div class="brand brand--header">Quorvel</div>
    <nav class="main-nav">
      <a href="#" style="left:863px">BLOG</a>
      <a href="#" style="left:923px">PODCAST</a>
      <a href="#" style="left:1040px">LOGIN</a>
    </nav>
  </header>

  <section class="signup-panel">
    <h1>Quorvel Pages</h1>
    <p class="lead">Build multiple Quorvel pages through one account for yourself,<br>your family and to keep loved one's legacies alive.</p>
    <h2>SIGNUP</h2>
    <input class="email-field" type="email" placeholder="Enter email address">
    <button class="subscribe-button" type="button">SUBSCRIBE</button>
  </section>

  <section class="features">
    <div class="feature" style="left:130px"><h3>Create</h3><p>Create Timelines,<br>Maps, Family Trees</p></div>
    <div class="divider" style="left:226px"></div>
    <div class="feature" style="left:324px"><h3>Memorialize</h3><p>Memorialize<br>Loved Ones</p></div>
    <div class="divider" style="left:421px"></div>
    <div class="feature" style="left:519px"><h3>Share</h3><p>Share Family Stories,<br>History and more</p></div>
    <div class="divider" style="left:618px"></div>
    <div class="feature" style="left:697px"><h3>Control</h3><p>Control<br>Your Privacy</p></div>
    <div class="divider" style="left:775px"></div>
    <div class="feature" style="left:888px"><h3>No Ads</h3><p>No Ads, No Like Buttons<br>No News Feeds</p></div>
  </section>

  <footer class="site-footer">
    <div class="brand brand--footer">Quorvel</div>
    <nav class="footer-links">
      <a href="#">Privacy Policy</a>
      <a href="#">Terms of Use</a>
      <a href="#">Data Tracking</a>
      <a href="#">Policy</a>
      <a href="#">Submit Feedback</a>
      <a href="#">Quorvel © 2017</a>
    </nav>
  </footer>
</div>
</body>
</html>
```